Health and Wellness Company Business Card

I need a business card design that is clean and uses modern minimalist style. The design should incorporate our logo (see attached). I would also like to use embossing on the cards so that they also have a great feel. I am open to the card using one or more colors, and these do not have to correspond to the colors in the concept paper. The card can either be one-sided or use both sides of the card.The logo uses the Avenir font.

I will need the file designed in Adobe CS and compatible with CS5.5 (Illustrator preferable) and I'll need the working file (for example: .ai) once the project is complete so that I can change the names/contact info/etc for each variation of the card.

This needs to be a memorable card for the recipient. They should think: "This is a great business card" either because of its simplicity or embossing effects or use of color.

Target Market(s)

The audience for our company has two main groups: people who pay for healthcare (insurers, companies, researcher companies) and people with chronic health conditions who are the consumers of our services and resources.

Industry/Entity Type

Business

Requirements
Must have
• Essential components of the card include: Company logo, contact Name (Mark Tolley), phone number (5808127346), email address (mtolley@brenquora.com), slogan/tagline that consists of ~30-40 characters (Use Lorem Ipsum)
Nice to have
• These fall just slightly short of "must have" to allow for design flexibility: Embossing or spot varnish effects and a splash of color
Should not have
• Designs with these components will not be successful: flashy or showy designs that are not professional in appearance, and lots of different colors

```html
<!DOCTYPE html>
<html lang="en">
<head>
<meta charset="utf-8">
<title>Brenquora Business Card</title>
<link href="https://fonts.googleapis.com/css2?family=Lato:wght@300;400&display=swap" rel="stylesheet">
<style>
  :root {
    --backdrop: #2b2b2d;
    --paper: #f4f4f5;
    --paper-shade: #e6e6e8;
    --ink: #6d6b7d;
    --ink-soft: #8a8896;
    --accent: #2e4a55;
  }
  * { box-sizing: border-box; margin: 0; padding: 0; }
  html, body {
    width: 1200px; height: 900px; overflow: hidden;
    background: var(--backdrop);
    font-family: "Lato", "Helvetica Neue", Arial, sans-serif;
  }
  .card {
    position: absolute;
    left: 330px;
    width: 540px; height: 309px;
    background: linear-gradient(135deg, var(--paper) 0%, var(--paper-shade) 100%);
    box-shadow: 0 14px 30px rgba(0,0,0,.45);
    overflow: hidden;
  }
  .card--contact { top: 110px; }
  .card--tagline { top: 480px; }

  /* contact side */
  .brand {
    position: absolute; left: 44px; top: 46px;
    display: flex; align-items: center; gap: 14px;
    color: var(--ink); font-weight: 400; font-size: 15px;
    letter-spacing: 0.55em; text-transform: uppercase;
  }
  .brand__mark { width: 26px; height: 26px; background: var(--ink); border-radius: 6px; }
  .person-name {
    position: absolute; left: 44px; top: 108px;
    color: var(--ink); font-weight: 300; font-size: 34px; letter-spacing: 0.02em;
    text-transform: uppercase;
  }
  .name-rule {
    position: absolute; left: 44px; top: 160px; width: 300px; height: 2px;
    background: var(--accent);
  }
  .name-rule::after {
    content: ""; position: absolute; right: -10px; top: -5px;
    width: 12px; height: 12px; background: var(--accent); border-radius: 3px;
  }
  .divider {
    position: absolute; left: 0; top: 198px; width: 100%; height: 1px;
    background: var(--accent); opacity: .7;
  }
  .contact {
    position: absolute; left: 44px; top: 214px;
    list-style: none; color: var(--ink); font-size: 14px; line-height: 24px;
  }
  .contact__label { display: inline-block; width: 60px; }

  /* tagline side */
  .pattern-field {
    position: absolute; left: 0; top: 0; width: 190px; height: 100%;
    background: linear-gradient(160deg, var(--ink) 0%, var(--ink-soft) 100%);
  }
  .frame-line { position: absolute; left: 0; top: 0; }
  .tagline {
    position: absolute; left: 236px; top: 158px;
    color: var(--ink); font-weight: 400; font-size: 30px; line-height: 36px;
    letter-spacing: 0.02em; text-transform: uppercase;
  }
</style>
</head>
<body>
  <section class="card card--contact" aria-label="Contact side">
    <div class="brand"><span class="brand__mark"></span><span>Brenquora</span></div>
    <h1 class="person-name">Mark Tolley</h1>
    <div class="name-rule"></div>
    <div class="divider"></div>
    <ul class="contact">
      <li><span class="contact__label">Phone:</span>5808127346</li>
      <li><span class="contact__label">Email:</span>mtolley@brenquora.com</li>
      <li><span class="contact__label">Web:</span>brenquora.com</li>
    </ul>
  </section>

  <section class="card card--tagline" aria-label="Tagline side">
    <div class="pattern-field" role="img" aria-label="Embossed field of rounded pebble shapes in slate grey"></div>
    <svg class="frame-line" width="540" height="309" viewBox="0 0 540 309" aria-hidden="true">
      <path d="M540 128 H236 Q206 128 206 158 V278" fill="none" stroke="var(--ink)" stroke-width="6"/>
      <rect x="196" y="276" width="22" height="22" rx="6" fill="var(--ink)"/>
    </svg>
    <p class="tagline">Your tagline<br>goes here</p>
  </section>
</body>
</html>
```